Plumvale CEO needs a Crowdsourced Graphic for a Wirelark Article

I need a simple graphic / banner for a blog post that's going to be posted on Wirelark (www.wirelark.com) - the biggest tech blog in the world.

The article will be written by Tobin Marsh (Plumvale's CEO) and the title will be "Asia's Secret Crowdsourcing Boom". The article is about the tens of thousands of people using crowdsourcing websites (like Plumvale.com, Qorvel.com and Vantrio.com) in China, India, the Philippines, Australia and other countries in the Asia Pacific region.

We'd really like to get this ASAP - so early submissions encouraged. We will try and get the winning designer linked to from the article.

Thanks to everyone that submitted!  Some great designs and hard to choose! :)

Target Market(s)

Tech saavy readers, English speakers

Industry/Entity Type

Tech

Requirements
Must have
• The graphic SHOULD:
1) Have the text "Asia's secret crowdsourcing boom" with some nice design and fonts (consider grey subtle pattern background and white drop shadow on fonts) - see attached examples
2) Have an Asian theme
3) Have the dimensions 640px wide by 240px wide
Nice to have
• The graphic COULD:
1) Have references to some or all of the countries mentioned above or use Asian characters as part of the background / motif (maybe the word "crowd" or "crowd sourcing" in different languages). In Chinese, the word for crowdsourcing is "witkey" (and there are corresponding Chinese characters: ??)
2) Emphasize the word "Asia" (using color and larger/different font)
3) Use a chart showing exponential (i.e. fast) growth - like the attached
4) Have a second line of text "5 Things You Didn't Know About Crowdsourcing in Asia"

```html
<!DOCTYPE html>
<html lang="en">
<head>
<meta charset="utf-8">
<title>Asia's Secret Crowdsourcing Boom</title>
<link rel="stylesheet" href="https://fonts.googleapis.com/css2?family=Alfa+Slab+One&family=Arimo:ital,wght@0,400;0,700;1,700&family=Roboto+Condensed:wght@700&display=swap">
<style>
  :root {
    --bg-light: #d4d4d2;
    --bg-mid: #a9aaa7;
    --bg-dark: #8a8b88;
    --map-green: #3f7a2a;
    --map-green-light: #6a9e4a;
    --title-yellow: #f6e81a;
    --title-orange: #e79a12;
    --title-outline: #2a2208;
    --ink: #111111;
    --glow: #ffffff;
    --sub-yellow: #eef21a;
    --bar-light: #d8f24a;
    --bar-mid: #8fcf1f;
    --bar-dark: #3f8a10;
  }
  html, body {
    margin: 0;
    padding: 0;
    overflow: hidden;
    background: #ffffff;
  }
  .banner {
    position: relative;
    width: 1200px;
    height: 450px;
    overflow: hidden;
    background:
      radial-gradient(ellipse at 45% 40%, var(--bg-light) 0%, var(--bg-mid) 60%, var(--bg-dark) 100%);
  }
  .asia-map {
    position: absolute;
    left: 0;
    top: 0;
    width: 480px;
    height: 310px;
    background: radial-gradient(ellipse at 30% 35%, var(--map-green-light) 0%, var(--map-green) 45%, rgba(63,122,42,0) 75%);
    opacity: 0.85;
  }
  .title-asia {
    position: absolute;
    left: 478px;
    top: 14px;
    margin: 0;
    font-family: "Alfa Slab One", serif;
    font-size: 104px;
    line-height: 1;
    letter-spacing: 2px;
    color: var(--title-yellow);
    background: linear-gradient(180deg, var(--title-yellow) 20%, var(--title-orange) 100%);
    -webkit-background-clip: text;
    background-clip: text;
    -webkit-text-fill-color: transparent;
    -webkit-text-stroke: 3px var(--title-outline);
    filter: drop-shadow(0 0 6px rgba(255,255,255,0.9));
  }
  .title-line {
    position: absolute;
    left: 208px;
    top: 140px;
    margin: 0;
    font-family: "Arimo", sans-serif;
    font-size: 44px;
    line-height: 1;
    color: var(--ink);
    text-transform: uppercase;
    white-space: nowrap;
    text-shadow: 0 0 6px var(--glow), 0 0 10px var(--glow), 0 0 14px var(--glow);
  }
  .title-line .word-secret { font-weight: 700; font-style: italic; }
  .title-line .word-crowd { font-weight: 400; letter-spacing: -1px; }
  .title-line .word-boom { font-weight: 700; }
  .subtitle {
    position: absolute;
    left: 36px;
    top: 250px;
    margin: 0;
    font-family: "Roboto Condensed", sans-serif;
    font-weight: 700;
    font-size: 35px;
    line-height: 44px;
    color: var(--sub-yellow);
    text-transform: uppercase;
    text-shadow: 1px 2px 3px rgba(0,0,0,0.45);
  }
  .growth-chart {
    position: absolute;
    left: 0;
    top: 0;
    width: 1200px;
    height: 450px;
  }
</style>
</head>
<body>
<div class="banner">
  <div class="asia-map" role="img" aria-label="Green map of Asia and the Pacific region"></div>

  <svg class="growth-chart" viewBox="0 0 1200 450" role="img" aria-label="Bar chart with an arrow showing fast growth">
    <defs>
      <linearGradient id="barFront" x1="0" y1="0" x2="1" y2="0">
        <stop offset="0" stop-color="var(--bar-light)"/>
        <stop offset="1" stop-color="var(--bar-mid)"/>
      </linearGradient>
      <linearGradient id="arrowFill" x1="0" y1="1" x2="1" y2="0">
        <stop offset="0" stop-color="var(--bar-mid)" stop-opacity="0.1"/>
        <stop offset="0.5" stop-color="var(--bar-mid)"/>
        <stop offset="1" stop-color="var(--bar-light)"/>
      </linearGradient>
    </defs>

    <path class="growth-arrow" fill="url(#arrowFill)"
      d="M640,306 Q890,262 1030,124 L1002,104 L1118,52 L1082,170 L1058,146 Q920,290 640,312 Z"/>

    <g class="bars">
      <g><polygon points="872,350 898,350 898,420 872,420" fill="url(#barFront)"/><polygon points="898,350 908,342 908,414 898,420" fill="var(--bar-dark)"/><polygon points="872,350 882,342 908,342 898,350" fill="var(--bar-light)"/></g>
      <g><polygon points="910,340 938,340 938,422 910,422" fill="url(#barFront)"/><polygon points="938,340 948,332 948,416 938,422" fill="var(--bar-dark)"/><polygon points="910,340 920,332 948,332 938,340" fill="var(--bar-light)"/></g>
      <g><polygon points="950,322 982,322 982,424 950,424" fill="url(#barFront)"/><polygon points="982,322 993,313 993,418 982,424" fill="var(--bar-dark)"/><polygon points="950,322 961,313 993,313 982,322" fill="var(--bar-light)"/></g>
      <g><polygon points="1002,272 1038,272 1038,426 1002,426" fill="url(#barFront)"/><polygon points="1038,272 1050,262 1050,420 1038,426" fill="var(--bar-dark)"/><polygon points="1002,272 1014,262 1050,262 1038,272" fill="var(--bar-light)"/></g>
      <g><polygon points="1106,246 1142,246 1142,428 1106,428" fill="url(#barFront)"/><polygon points="1142,246 1154,236 1154,422 1142,428" fill="var(--bar-dark)"/><polygon points="1106,246 1118,236 1154,236 1142,246" fill="var(--bar-light)"/></g>
    </g>
  </svg>

  <h1 class="title-asia">Asia's</h1>
  <p class="title-line"><span class="word-secret">Secret</span> <span class="word-crowd">Crowdsourcing</span> <span class="word-boom">Boom</span></p>
  <p class="subtitle">5 Things You Didn't Know<br>About Crowdsourcing in Asia</p>
</div>
</body>
</html>
```